Tax & Accounting business needs business card design

Looking for a professional classy business card for a tax and accounting business. We offer quality, professional services to individuals and small businesses including tax preparation and planning, accounting and bookkeeping, payroll services, and business consulting.

I am an Enrolled Agent (EA) which is a Federally Licensed Tax Practitioner. I am licensed to represent taxpayers before the ZTQ.

We want to stand out from all the other "boring" tax & accounting firms without being over the top.

We have a well established firm in one location and are now opening a second location.

• Logo
• Logo color scheme
• Both location addresses
• Front and back of card
• Please see my sample business card (attached) for location addresses, phone numbers, ect. Although you may get some inspiration from this sample card, this is my own unqualified and bad attempt at designing my own card which I'm not happy with.

```html
<!DOCTYPE html>
<html lang="en">
<head>
<meta charset="utf-8">
<title>Tally &amp; Ledger Solutions – Business Card</title>
<link rel="stylesheet" href="https://fonts.googleapis.com/css2?family=Arimo:wght@400&family=Tinos:ital,wght@0,400;0,700;1,400&display=swap">
<style>
  :root {
    --teal: #0f5f57;
    --teal-deep: #0b4a44;
    --charcoal: #3c3c3e;
    --ink: #2e2e2e;
    --grey-text: #4a4a4a;
    --paper: #fbfbfa;
    --stage: #e6e6e4;
  }
  * { box-sizing: border-box; margin: 0; padding: 0; }
  html, body { width: 1200px; height: 1028px; overflow: hidden; }
  body {
    background: var(--stage);
    position: relative;
    font-family: "Arimo", Arial, sans-serif;
    color: var(--ink);
  }
  .card {
    position: absolute;
    background: var(--paper);
    border-radius: 18px;
    overflow: hidden;
    box-shadow: 0 6px 18px rgba(0,0,0,.18);
  }

  /* Back side (horizontal) */
  .card-back { left: 50px; top: 300px; width: 580px; height: 330px; }
  .card-back svg.waves { position: absolute; inset: 0; }
  .credentials {
    position: absolute; left: 28px; top: 28px;
    font-size: 15px; letter-spacing: 1.5px; line-height: 1.25;
    color: var(--grey-text);
  }
  .services {
    position: absolute; left: 0; right: 0; top: 100px;
    text-align: center; font-family: "Tinos", "Times New Roman", serif;
    color: var(--teal);
  }
  .services .headline { font-size: 22px; }
  .services .lines { font-size: 23px; }
  .services .audience { font-style: italic; font-size: 16px; letter-spacing: .5px; }
  .services .web {
    font-family: "Arimo", Arial, sans-serif; font-size: 15px;
    letter-spacing: 2px; margin-top: 18px;
  }
  .licence {
    position: absolute; right: 26px; top: 226px;
    font-size: 13px; letter-spacing: 1px; color: var(--grey-text);
    text-align: right; width: 260px; line-height: 1.35;
  }

  /* Front side (vertical) */
  .card-front { left: 700px; top: 190px; width: 380px; height: 650px; padding: 44px 34px; }
  .brand {
    display: flex; align-items: center; gap: 12px;
    font-family: "Tinos", "Times New Roman", serif; font-weight: 700;
    color: var(--teal); font-size: 30px; line-height: 1.05;
  }
  .brand .mark { width: 18px; height: 18px; border-radius: 50%; background: var(--teal); flex: none; }
  .person {
    margin-top: 48px;
    font-family: "Tinos", "Times New Roman", serif; font-weight: 700;
    font-size: 29px; color: var(--teal);
  }
  .email { font-size: 16px; letter-spacing: 1px; color: var(--grey-text); margin-top: 4px; }
  .office { margin-top: 34px; font-size: 19px; line-height: 1.32; letter-spacing: .8px; color: var(--ink); }
  .office h2 { font-weight: 400; font-size: 19px; color: var(--teal); }
</style>
</head>
<body>

  <section class="card card-back" aria-label="Card back">
    <svg class="waves" width="580" height="330" viewBox="0 0 580 330" aria-hidden="true">
      <path d="M300 0 H580 V170 C545 70 440 18 300 0 Z" fill="var(--charcoal)"/>
      <path d="M0 165 C130 250 320 300 520 330 H0 Z" fill="var(--teal)"/>
      <path d="M0 190 C140 270 330 310 470 330 H0 Z" fill="var(--teal-deep)"/>
    </svg>
    <p class="credentials">Enrolled Agent<br>Federally Licensed Tax Practitioner</p>
    <div class="services">
      <p class="headline">Professional Business Services</p>
      <p class="lines">Taxes - Accounting - Bookkeeping - Payroll</p>
      <p class="audience">for individuals and small businesses</p>
      <p class="web">www.tallyledger-pv.com</p>
    </div>
    <p class="licence">Licensed to represent Taxpayers before the ZTQ</p>
  </section>

  <section class="card card-front" aria-label="Card front">
    <div class="brand"><span class="mark"></span><span>Tally &amp; Ledger<br>Solutions LLC</span></div>
    <p class="person">Marisol T. Vega, EA</p>
    <p class="email">marisol@tallyledgerpv.com</p>
    <div class="office">
      <h2>Cedar Ridge Office</h2>
      <p>4410 Cerrillos Rd Ste B</p>
      <p>ofc 505.555.0146</p>
      <p>fax 505.555.0147</p>
    </div>
    <div class="office">
      <h2>Piñon Valley Office</h2>
      <p>3870 Juan Tabo Blvd NE</p>
      <p>Piñon Valley, NM 87599</p>
      <p>ofc 505.555.0188</p>
      <p>fax 505.555.0177</p>
    </div>
  </section>

</body>
</html>
```